Conference for Teenagers Needs Event Graphics

I am in need of event graphics for our upcoming event. This event, titled "Kestrel Youth Rally", is a weekend event for teenagers 11-19 years old. They hear from speakers, listen to a band, and do other fun activities. Our theme is "Together." Graphic design should have a young adult/older teen feel. Clean, not very bright colors.

Event Info:
November 6-8, 2020
Pellworth Exhibit Hall, Sioux Falls, SD
Speakers: TBD (will give name and picture before final approval)
Worship: (band name TBD before final approval)
KestrelYouthRally.com
#417KR
Our Organization Logo (attached): Lumen Forward

Once designed, I need the following graphics file sizes:
-11x17 Vertical Poster design: include all event info AND a "blank" spot/box for groups to add their own details/information. Also include the QRV logo and our organization logo Lumen Forward in someway.
-4x3 horizontal postcard: include all event info on 1 side including LumenForward logo and QRV; blank backside
-Main Graphic Slide: formatted to fit a widescreen 16x9 screen. Include event name, hashtag, QRV and Lumen Forward logo
-social media graphics for event: can incorporate some or all of the event details
-4.25x 2.75 vertical badge: include event title on front with Lumen Forward logo

Target Market(s)

Young adults or older teenagers

Requirements
Must have
• -event info
-Lumen Forward Logo & QRV logo

```html
<!DOCTYPE html>
<html lang="en">
<head>
<meta charset="utf-8">
<title>Kestrel Youth Rally – Poster</title>
<link rel="stylesheet" href="https://fonts.googleapis.com/css2?family=Stardos+Stencil:wght@700&family=Open+Sans:wght@400;700&family=Oswald:wght@700&display=swap">
<style>
  :root {
    --ink: #111111;
    --paper: #ffffff;
    --orange: #ee5a2a;
    --yellow: #f6e93a;
    --blue: #2e7ea6;
    --green: #6db443;
    --grey: #808082;
    --grey-light: #bdbdc0;
    --brand-blue: #2fb4e8;
  }
  * { margin: 0; padding: 0; box-sizing: border-box; }
  html, body { width: 776px; height: 1200px; overflow: hidden; background: var(--paper); }
  .poster {
    position: relative;
    width: 776px;
    height: 1200px;
    border: 2px solid var(--ink);
    background: var(--paper);
    font-family: "Open Sans", Arial, sans-serif;
    color: var(--ink);
  }
  .footprints {
    position: absolute;
    left: 58px;
    top: 34px;
    width: 690px;
    height: 545px;
    border-radius: 18px;
    background: linear-gradient(160deg,
      rgba(238,90,42,.35) 0%,
      rgba(246,233,58,.35) 28%,
      rgba(46,126,166,.3) 48%,
      rgba(109,180,67,.3) 66%,
      rgba(128,128,130,.3) 82%,
      rgba(189,189,192,.25) 100%);
  }
  .event-title {
    position: absolute;
    left: 48px;
    top: 400px;
    font-family: "Stardos Stencil", "Courier New", monospace;
    font-weight: 700;
    font-size: 92px;
    line-height: 76px;
    letter-spacing: 4px;
    text-transform: uppercase;
  }
  .event-title span { display: block; }
  .event-when, .event-where {
    position: absolute;
    left: 52px;
    font-weight: 700;
    font-size: 33px;
    letter-spacing: -1px;
  }
  .event-when { top: 730px; }
  .event-where { top: 773px; }
  .lineup {
    position: absolute;
    left: 48px;
    right: 30px;
    font-size: 27px;
    line-height: 41px;
  }
  .lineup strong { font-weight: 700; }
  .lineup--speakers { top: 834px; }
  .lineup--worship { top: 930px; left: 57px; }
  .partners {
    position: absolute;
    left: 54px;
    right: 38px;
    top: 1020px;
    height: 100px;
    display: flex;
    align-items: center;
    justify-content: space-between;
  }
  .org-name {
    font-weight: 700;
    font-size: 24px;
    line-height: 28px;
    color: var(--brand-blue);
    width: 150px;
  }
  .slogan {
    font-family: "Oswald", Impact, sans-serif;
    font-weight: 700;
    font-size: 34px;
    letter-spacing: 1px;
    text-transform: uppercase;
  }
  .partner-name {
    display: flex;
    align-items: center;
    gap: 8px;
    font-weight: 700;
    font-size: 40px;
    color: var(--ink);
  }
  .partner-name .dot {
    width: 12px; height: 12px; border-radius: 50%; background: var(--ink);
  }
  .site-link, .hashtag {
    position: absolute;
    top: 1130px;
    font-size: 31px;
    letter-spacing: 1px;
  }
  .site-link { left: 54px; }
  .hashtag { right: 48px; }
</style>
</head>
<body>
  <main class="poster">
    <div class="footprints" role="img" aria-label="Trail of six bare footprints in orange, yellow, blue, green, grey and light grey walking across the page"></div>

    <h1 class="event-title">
      <span>Kestrel</span>
      <span>Youth</span>
      <span>Rally</span>
    </h1>

    <p class="event-when">November 6-8, 2020</p>
    <p class="event-where">Pellworth Exhibit Hall, Sioux Falls, SD</p>

    <p class="lineup lineup--speakers"><strong>Speakers:</strong> TBD (will give name and picture before final approval)</p>
    <p class="lineup lineup--worship"><strong>Worship:</strong> (band name TBD before final approval)</p>

    <div class="partners">
      <div class="org-name">Lumen Forward</div>
      <div class="slogan">Together We Can</div>
      <div class="partner-name"><span class="dot"></span>QRV</div>
    </div>

    <p class="site-link">KestrelYouthRally.com</p>
    <p class="hashtag">#417KR</p>
  </main>
</body>
</html>
```